Business cards and letterhead
UK size business cards/letterhead
Project: Business cards and letterhead
Business cards and letterhead - Information Technology
Creative Brief
Professional
Gareth Pellow
Director
148 Ashcombe Lane Twickenham Middlesex TW4 3QR
gareth.pellow@corvalisen.com
www.corvalisen.com
Note business card needs to be UK-sized (i.e. 85 x 55)/double sided, and the letterhead suitable for A4 paper Back of card can contain some/all of suggested text, depending upon how well it fits
ECM Consultancy Services - Project Management and Delivery - Implementation Planning - Data Conversion Management - Existing System Reviews - Software Design and Development - Test Strategy Definition and Execution

```html
<!DOCTYPE html>
<html lang="en">
<head>
<meta charset="utf-8">
<title>Corvalisen – Business Card</title>
<link href="https://fonts.googleapis.com/css2?family=Open+Sans:wght@400;600;700&display=swap" rel="stylesheet">
<style>
  :root {
    --backdrop: #e9e6e1;
    --card: #ffffff;
    --brand-blue: #1c8fc4;
    --brand-blue-deep: #0b5f8f;
    --silver: #b9bcc0;
    --silver-dark: #7d8185;
    --ink: #3b3e42;
    --ink-soft: #6a6e73;
    --rule: #d3d5d8;
  }
  * { margin: 0; padding: 0; box-sizing: border-box; }
  html, body {
    width: 1200px; height: 780px; overflow: hidden;
    background: var(--backdrop);
    font-family: "Open Sans", Arial, sans-serif;
  }
  .card {
    position: absolute; left: 100px; top: 67px;
    width: 1000px; height: 646px;
    background: var(--card);
    border-radius: 26px;
    overflow: hidden;
    box-shadow: 0 8px 24px rgba(0,0,0,0.18);
  }
  .card-bands { position: absolute; inset: 0; }
  .brand {
    position: absolute; left: 130px; top: 190px; width: 320px;
    text-align: center;
  }
  .brand-mark {
    width: 130px; height: 130px; margin: 0 auto 26px;
    border-radius: 50%; background: var(--brand-blue);
  }
  .brand-name {
    font-weight: 700; font-size: 40px; letter-spacing: 1px;
    color: var(--ink);
  }
  .divider {
    position: absolute; left: 482px; top: 110px;
    width: 2px; height: 430px;
    background: linear-gradient(var(--card), var(--rule) 20%, var(--rule) 80%, var(--card));
  }
  .details { position: absolute; left: 515px; top: 112px; color: var(--ink-soft); }
  .person-name { font-size: 34px; font-weight: 600; color: var(--brand-blue-deep); line-height: 1.2; }
  .person-role { font-size: 21px; margin-bottom: 58px; }
  .address { font-size: 21px; line-height: 1.35; font-style: normal; margin-bottom: 30px; }
  .contact-list { list-style: none; font-size: 21px; line-height: 1.6; }
  .contact-list li { display: flex; align-items: center; gap: 12px; }
  .contact-icon { width: 20px; height: 20px; flex: none; }
</style>
</head>
<body>
  <div class="card">
    <svg class="card-bands" width="1000" height="646" viewBox="0 0 1000 646" aria-hidden="true">
      <defs>
        <linearGradient id="band-blue" x1="0" y1="0" x2="1" y2="1">
          <stop offset="0" stop-color="#2aa6d8"/>
          <stop offset="1" stop-color="#0b5f8f"/>
        </linearGradient>
        <linearGradient id="band-silver" x1="0" y1="0" x2="0" y2="1">
          <stop offset="0" stop-color="#e2e4e6"/>
          <stop offset="0.5" stop-color="#8d9195"/>
          <stop offset="1" stop-color="#d6d8db"/>
        </linearGradient>
      </defs>
      <path d="M0,0 H105 Q30,323 105,646 H0 Z" fill="url(#band-blue)"/>
      <path d="M105,0 Q30,323 105,646" fill="none" stroke="url(#band-silver)" stroke-width="16"/>
      <path d="M1000,0 H905 Q975,323 905,646 H1000 Z" fill="url(#band-blue)"/>
      <path d="M905,0 Q975,323 905,646" fill="none" stroke="url(#band-silver)" stroke-width="16"/>
    </svg>

    <div class="brand">
      <div class="brand-mark"></div>
      <div class="brand-name">CORVALISEN</div>
    </div>

    <div class="divider"></div>

    <div class="details">
      <div class="person-name">Gareth Pellow</div>
      <div class="person-role">Director</div>
      <address class="address">148 Ashcombe Lane,<br>Twickenham<br>Middlesex, TW4 3QR</address>
      <ul class="contact-list">
        <li>
          <svg class="contact-icon" viewBox="0 0 20 20" aria-hidden="true"><path d="M5 2 L8 2 L9 6 L7 8 Q9 12 12 13 L14 11 L18 12 L18 15 Q18 18 15 18 Q3 17 2 5 Q2 2 5 2 Z" fill="var(--brand-blue-deep)"/></svg>
          +44-7700-900-418
        </li>
        <li>
          <svg class="contact-icon" viewBox="0 0 20 20" aria-hidden="true"><rect x="1" y="4" width="18" height="12" rx="2" fill="var(--brand-blue-deep)"/><path d="M2 5 L10 11 L18 5" fill="none" stroke="#fff" stroke-width="1.5"/></svg>
          gareth.pellow@corvalisen.com
        </li>
        <li>
          <svg class="contact-icon" viewBox="0 0 20 20" aria-hidden="true"><circle cx="10" cy="10" r="9" fill="var(--brand-blue)"/><path d="M1 10 H19 M10 1 Q4 10 10 19 M10 1 Q16 10 10 19" fill="none" stroke="#fff" stroke-width="1.2"/></svg>
          www.corvalisen.com
        </li>
      </ul>
    </div>
  </div>
</body>
</html>
```